Roofing Contractor business card redesign

I want to redesign my business card with a fresh, eye catching concept

Target Market(s)

Residential Roofing Clients, potential employees, and subcontractors.

Industry/Entity Type

Business

Colors

Designer to choose colors to be used in the design.

Requirements
Nice to have
• I just want something that's more pleasing to the eye. You can use a combination of either / or of my logos.

```html
<!DOCTYPE html>
<html lang="en">
<head>
<meta charset="utf-8">
<title>Steady Crew Builders – Business Card</title>
<link rel="stylesheet" href="https://fonts.googleapis.com/css2?family=Oswald:wght@500;700&family=Roboto:wght@400&display=swap">
<style>
  :root {
    --bg: #1b1b1b;
    --orange: #e8822a;
    --orange-light: #f08a2c;
    --brown: #4a1409;
    --brown-dark: #3a0f07;
    --ink: #333333;
    --white: #ffffff;
  }
  * { margin: 0; padding: 0; box-sizing: border-box; }
  html, body { width: 1200px; height: 963px; overflow: hidden; background: var(--bg); }
  .canvas { position: relative; width: 1200px; height: 963px; }

  .card {
    position: absolute;
    top: 332px;
    width: 520px;
    height: 298px;
    border-radius: 16px;
    overflow: hidden;
  }

  /* Front */
  .card--front { left: 50px; background: var(--white); }
  .front__logo {
    position: absolute; left: 34px; top: 58px;
    width: 190px; height: 150px;
    display: flex; flex-direction: column; align-items: center; justify-content: center; gap: 10px;
  }
  .front__logo-mark { width: 70px; height: 70px; border-radius: 50%; background: var(--brown); }
  .wordmark {
    font-family: "Oswald", sans-serif; font-weight: 700;
    color: var(--brown); text-align: center; line-height: 1.05;
  }
  .front__logo .wordmark { font-size: 26px; }
  .front__logo .wordmark small { display: block; font-size: 13px; letter-spacing: 0.02em; }

  .front__divider {
    position: absolute; left: 248px; top: 52px;
    width: 2px; height: 150px; background: var(--orange);
  }
  .front__details { position: absolute; left: 272px; top: 56px; }
  .front__name {
    font-family: "Oswald", sans-serif; font-weight: 500;
    font-size: 26px; color: var(--orange); letter-spacing: 0.02em; line-height: 1.1;
  }
  .front__lines {
    font-family: "Roboto", sans-serif; font-size: 14px; color: var(--ink);
    line-height: 1.32; margin-top: 4px;
  }
  .front__contacts { list-style: none; margin-top: 6px; }
  .front__contacts li {
    display: flex; align-items: center; gap: 8px;
    font-family: "Roboto", sans-serif; font-size: 14px; color: var(--ink); line-height: 1.35;
  }
  .front__contacts svg { width: 11px; height: 11px; flex: none; }

  .front__band {
    position: absolute; left: 0; bottom: 0; width: 100%; height: 34px;
    background: var(--brown-dark);
  }
  .front__band::before, .front__band::after {
    content: ""; position: absolute; bottom: 0; width: 70px; height: 14px; background: var(--orange);
  }
  .front__band::before { left: 0; }
  .front__band::after { right: 0; }

  /* Back */
  .card--back {
    left: 630px;
    background: linear-gradient(135deg, var(--orange-light), #d9711f);
    display: flex; align-items: center; justify-content: center;
  }
  .back__lockup { display: flex; flex-direction: column; align-items: center; gap: 4px; }
  .back__row { display: flex; align-items: center; gap: 14px; }
  .back__mark { width: 64px; height: 64px; border-radius: 50%; background: var(--brown); }
  .card--back .wordmark { font-size: 52px; }
  .back__tag {
    font-family: "Oswald", sans-serif; font-weight: 700;
    font-size: 22px; color: var(--brown); letter-spacing: 0.02em;
  }
</style>
</head>
<body>
<div class="canvas">

  <section class="card card--front" aria-label="Business card front">
    <div class="front__logo">
      <div class="front__logo-mark"></div>
      <div class="wordmark">Steady Crew<small>Builders, Inc.</small></div>
    </div>
    <div class="front__divider"></div>
    <div class="front__details">
      <h1 class="front__name">SAM HARLOW</h1>
      <p class="front__lines">
        Ridgeline Certified Roof Inspector<br>
        Licensed Property Adjuster<br>
        4180 Cedar Mill Road<br>
        Suite 110 Plano, TX 75093
      </p>
      <ul class="front__contacts">
        <li>
          <svg viewBox="0 0 12 12"><path d="M2.5 1 L4.5 1 L5.2 3.6 L4 4.6 Q5 7 7.4 8 L8.4 6.8 L11 7.5 L11 9.5 Q10.5 11 9 11 Q1 10 1 2.5 Q1 1 2.5 1Z" fill="#e8822a"/></svg>
          (555) 014-2200
        </li>
        <li>
          <svg viewBox="0 0 12 12"><rect x="3" y="0.8" width="6" height="10.4" rx="1" fill="none" stroke="#e8822a" stroke-width="1.3"/><circle cx="6" cy="9.2" r="0.7" fill="#e8822a"/></svg>
          (555) 018-7731
        </li>
        <li>
          <svg viewBox="0 0 12 12"><rect x="0.8" y="2.3" width="10.4" height="7.4" fill="none" stroke="#e8822a" stroke-width="1.2"/><path d="M0.8 2.3 L6 6.5 L11.2 2.3" fill="none" stroke="#e8822a" stroke-width="1.2"/></svg>
          sam@steadycrewtx.com
        </li>
      </ul>
    </div>
    <div class="front__band"></div>
  </section>

  <section class="card card--back" aria-label="Business card back">
    <div class="back__lockup">
      <div class="back__row">
        <div class="wordmark">Steady Crew</div>
        <div class="back__mark"></div>
      </div>
      <div class="back__tag">Builders, Inc.</div>
    </div>
  </section>

</div>
</body>
</html>
```